LANDING PAGE on a Word Press platform.

I have a website, www.thecalmledgermerchant.com and need to create a new landing page. I purchased a new url, www.calmledgermerchant.com and set it up on Word Press. It has a theme (I was trying to do it myself, but gave up) but you can change it if you need to. I will give you access so you can work directly on the Word Press Platform. Please visit my site, www.thecalmledgermerchant, so you can see what we are selling.
Updates

Thank you for being so patient. Unfortunately I had some pressing personal problems and had to leave the country for a couple of weeks. I am back now and will choose a design today. Thank you again!

Target Market(s)

Stock Market, High Worth Individuals, Traders, Investors

Requirements
Must have
• My landing page must look very professional and rich. I am sending a copy of my logo but the "the" before The Calm Ledger Merchant, needs to be removed. Some testimonials and services we provide. (all found on my home page)
Nice to have
• I am open to a new color scheme if possible. The logo colors would have to be changed.
Should not have
• Should not be too busy with too many images or text. I want a clean and easy to read landing page

```html
<!DOCTYPE html>
<html lang="en">
<head>
<meta charset="utf-8">
<title>The Calm Ledger Merchant – Landing Page</title>
<link rel="stylesheet" href="https://fonts.googleapis.com/css2?family=Open+Sans:wght@400;600;700;800&family=Arimo:wght@400;700&display=swap">
<style>
:root{
  --navy:#1c3a8a;
  --royal:#1f4fae;
  --sky:#2e9fe6;
  --sky-dark:#1a7fc4;
  --gold:#f7c623;
  --orange:#d3440f;
  --green:#2f7a12;
  --amber:#cf8a0b;
  --text:#222;
  --link:#1b8bd8;
  --page:#eceef2;
  --line:#cfd3da;
  --white:#fff;
}
*{box-sizing:border-box;margin:0;padding:0}
html,body{width:1200px;height:1000px;overflow:hidden}
body{position:relative;background:var(--page);font-family:"Arimo",Arial,sans-serif;color:var(--text)}
.abs{position:absolute}
.top-band{left:0;top:0;width:1200px;height:130px;background:linear-gradient(#eef6fc,#fff 40px)}
.brand{left:193px;top:16px;width:201px;height:63px;border:3px solid var(--royal);border-radius:10px;background:#fff;display:flex;align-items:center;gap:10px;padding-left:10px}
.brand-dot{width:40px;height:40px;border-radius:50%;background:var(--royal)}
.brand-name{font-family:"Open Sans",sans-serif;font-weight:700;font-size:17px;line-height:19px;color:var(--navy)}
.contact{right:198px;top:12px;text-align:right;color:var(--sky-dark);font-size:11px;line-height:13px}
.contact .call{font-family:"Open Sans",sans-serif;font-size:21px;font-weight:700;color:var(--sky);margin-top:6px;line-height:26px}
.contact .call b{color:var(--navy);font-size:24px}
.contact .city{color:var(--navy);font-size:10px}
.social{left:931px;top:99px;display:flex;gap:3px}
.social span{width:15px;height:15px;background:#3d5a98}
.social span:nth-child(2){background:#2aa3dd}
.social span:nth-child(3){background:#0e76a8}
.social span:nth-child(4){background:#d34836}
.nav{left:193px;top:98px;display:flex;gap:2px}
.nav a{display:block;height:32px;line-height:32px;text-align:center;white-space:nowrap;background:var(--navy);color:#fff;font-size:11px;text-decoration:none;clip-path:polygon(0 0,calc(100% - 8px) 0,100% 8px,100% 100%,0 100%)}
.nav a:nth-child(1){width:58px}
.nav a:nth-child(2){width:123px}
.nav a:nth-child(3){width:101px}
.nav a:nth-child(4){width:84px}
.nav a:nth-child(5){width:82px}
.nav a:nth-child(6){width:90px}
.hero{left:193px;top:130px;width:552px;height:242px;background:linear-gradient(160deg,#2461c9,#13379a 70%,#0f2c80);overflow:hidden}
.hero-title{left:59px;top:15px;width:242px;text-align:center;font-family:"Open Sans",sans-serif;font-weight:700;color:#fff;font-size:16px;line-height:20px;letter-spacing:-0.2px;white-space:nowrap}
.hero-title em{font-style:normal;color:var(--gold)}
.hero-price{left:306px;top:8px;font-family:"Open Sans",sans-serif;font-weight:800;color:var(--gold);font-size:58px;line-height:66px;letter-spacing:-1px}
.hero-sub{left:98px;top:60px;color:#fff;font-size:10px}
.hero-sub b{color:var(--gold)}
.gift{left:70px;top:90px;width:128px;height:79px;background:linear-gradient(135deg,#3dd49a,#17a86e)}
.gift-label{left:70px;top:152px;width:128px;text-align:center;white-space:nowrap;font-family:"Open Sans",sans-serif;font-weight:700;font-size:9px;color:#fff}
.perks{left:210px;top:87px;list-style:none;color:#fff;font-size:11px;line-height:16px}
.perks li::before{content:"";display:inline-block;width:5px;height:5px;border-radius:50%;background:var(--gold);margin-right:8px;vertical-align:2px}
.fist{left:450px;top:52px;width:102px;height:190px;background:linear-gradient(#e9c5a8,#1c1c2a 55%)}
.chart{left:0;top:80px}
.features{left:193px;top:372px;width:552px;height:73px;background:#fff}
.feat{top:-14px;width:90px;text-align:center;font-size:10px}
.feat svg{display:block;margin:0 auto 6px}
.login{left:745px;top:121px;width:257px;height:349px;background:var(--sky);color:#fff;text-align:center;border-right:6px solid var(--royal)}
.login h2{font-family:"Open Sans",sans-serif;font-weight:600;font-size:14px;margin-top:12px}
.login .note{font-size:10px;margin-top:4px}
.login hr{border:0;border-top:1px solid rgba(255,255,255,.5);margin:14px 8px 0}
.field{display:flex;align-items:center;justify-content:flex-end;gap:6px;margin:9px 12px 0 0;font-size:10px;font-weight:700}
.field i{display:block;width:166px;height:21px;background:#fff}
.login .btn{display:inline-block;margin-top:14px;width:130px;height:27px;line-height:27px;background:var(--navy);font-family:"Open Sans",sans-serif;font-size:14px;clip-path:polygon(6px 0,calc(100% - 6px) 0,100% 50%,calc(100% - 6px) 100%,6px 100%,0 50%)}
.login .info{font-size:10px;line-height:14px;padding:0 18px;margin-top:20px}
.login .call{text-align:left;padding-left:40px;font-family:"Open Sans",sans-serif;font-size:14px;margin-top:16px}
.login .call b{color:var(--gold);font-weight:600;font-size:17px;margin-left:8px}
.login .mail{text-align:left;padding-left:10px;font-family:"Open Sans",sans-serif;font-size:12px;margin-top:6px}
.login .mail b{color:var(--gold);font-weight:600}
.subscribe-head{left:193px;top:463px;font-family:"Open Sans",sans-serif;font-weight:600;font-size:16px;color:var(--navy)}
.plan{top:496px;width:107px;height:106px;color:#fff;text-align:center}
.plan .amt{font-family:"Open Sans",sans-serif;font-weight:800;font-size:38px;color:var(--gold);line-height:50px;margin-top:6px;letter-spacing:-1px}
.plan .amt sup{font-size:18px;vertical-align:14px}
.plan .term{font-size:10px;font-family:"Open Sans",sans-serif;font-weight:600}
.plan .go{display:block;margin:7px auto 0;width:76px;height:20px;line-height:20px;background:#fff;font-size:12px;clip-path:polygon(4px 0,calc(100% - 4px) 0,100% 50%,calc(100% - 4px) 100%,4px 100%,0 50%)}
.trial{left:745px;top:494px;width:261px;height:112px;background:var(--orange);color:#fff}
.trial-photo{left:10px;top:2px;width:85px;height:110px;background:linear-gradient(#6b3a22,#d9a683 55%,#f3efe9)}
.trial-text{left:90px;top:14px;font-family:"Open Sans",sans-serif;font-size:12px;line-height:17px}
.trial-text b{display:block;font-weight:700}
.trial-text .gold{color:var(--gold);font-weight:800}
.trial-text .hrs{font-family:"Arimo",sans-serif;font-size:11px;line-height:12px;margin-top:2px}
.trial-text .num{font-size:20px;line-height:26px}
.welcome{left:193px;top:628px;width:512px;border-top:1px solid var(--line);border-bottom:1px solid var(--line);padding:8px 0 6px}
.welcome h1{font-family:"Open Sans",sans-serif;font-weight:400;font-size:16px;color:var(--navy);margin-bottom:16px}
.welcome p{font-size:11px;line-height:16px;margin-bottom:16px}
.welcome a{color:var(--link);text-decoration:none}
.welcome a.u{text-decoration:underline}
.quote{left:745px;top:629px;width:261px;height:210px;background:#fff;border:1px solid var(--line);padding:0 14px}
.quote h3{font-family:"Open Sans",sans-serif;font-weight:400;font-size:16px;color:var(--navy);border-bottom:1px solid var(--line);margin:0 -14px;padding:8px 14px 6px}
.quote p{font-size:11px;line-height:16px;text-align:justify;margin-top:10px}
.quote .by{color:var(--sky-dark);font-weight:700;font-size:11px;margin-top:4px}
.quote .arrows{right:18px;bottom:18px;color:#666;font-size:14px;letter-spacing:8px}
.cta{top:862px;height:55px;background:#fff;border:1px solid var(--line);border-radius:8px}
.cta-trial{left:193px;width:396px;text-align:center}
.cta-trial .big{font-family:"Open Sans",sans-serif;font-weight:700;font-size:17px;color:var(--navy);margin-top:6px}
.cta-trial .big b{color:var(--green);font-size:25px}
.cta-trial .small{font-size:10px;color:var(--navy);font-weight:700}
.cta-news{left:611px;width:395px;padding:6px 16px}
.cta-news .lbl{font-size:10px;font-weight:700;color:var(--navy)}
.cta-news .row{display:flex;gap:8px;margin-top:3px;align-items:center}
.cta-news .in{width:134px;height:23px;border:1px solid #bbb;font-size:10px;padding:5px 6px;color:#555}
.cta-news .in span{color:#d00}
.cta-news .send{margin-left:2px;width:76px;height:23px;line-height:23px;background:#111;color:#fff;text-align:center;font-weight:700;font-size:12px;clip-path:polygon(0 0,100% 0,96% 50%,100% 100%,0 100%,4% 50%)}
.footer{left:0;top:943px;width:1200px;height:57px;background:linear-gradient(#2c4fa3,#1c3a8a);color:#fff;text-align:center}
.footer nav{margin-top:19px;font-size:9px}
.footer nav a{color:#fff;text-decoration:none;margin:0 3px}
.footer small{display:block;margin-top:5px;font-size:7px;color:#b9c6e6}
</style>
</head>
<body>
<div class="abs top-band"></div>

<div class="abs brand"><span class="brand-dot"></span><span class="brand-name">CALM LEDGER<br>MARKET</span></div>

<div class="abs contact">Mail us at<br>info@calmledgermerchant.com
  <div class="call">CALL NOW! <b>555-014-2277</b></div>
  <div class="city">Brookfield, NY 10999</div>
</div>

<div class="abs social" aria-label="Social links"><span></span><span></span><span></span><span></span></div>

<nav class="abs nav">
  <a href="#">ABOUT</a><a href="#">CURRENT PORTFOLIO</a><a href="#">LATEST REPORT</a><a href="#">WATCH LIST</a><a href="#">DAILY TICKER</a><a href="#">MARKET NEWS</a>
</nav>

<section class="abs hero">
  <svg class="abs chart" width="552" height="162" viewBox="0 0 552 162">
    <polyline points="0,150 40,138 70,146 110,118 140,128 180,108 215,118 250,92 280,102 320,82 350,94 390,68 420,78 460,46 490,56 530,4" fill="none" stroke="#e0231f" stroke-width="4"/>
  </svg>
  <div class="abs hero-title">BECOME <em>A PAID</em> SUBSCRIBER<br>MONTHLY SUBSCRIPTION AT</div>
  <div class="abs hero-price">$150</div>
  <div class="abs hero-sub">Subscribe for Two Week <b>FREE</b> trial today.</div>
  <div class="abs gift" role="img" aria-label="Wrapped gift card with red ribbon"></div>
  <div class="abs gift-label">FOR 2 WEEKS FREE TRIAL</div>
  <ul class="abs perks">
    <li>Daily Email Updates on Current Positions</li>
    <li>Private Chirper Feed for Traders</li>
    <li>TCLM 15 Fab Index</li>
    <li>Weekly Report</li>
    <li>Live Feed on Market News</li>
  </ul>
  <div class="abs fist" role="img" aria-label="Raised fist of a businessman in a suit"></div>
</section>

<section class="abs features">
  <div class="abs feat" style="left:40px">
    <svg width="52" height="52" viewBox="0 0 52 52"><polygon points="16,1 36,1 51,16 51,36 36,51 16,51 1,36 1,16" fill="#333" stroke="#fff" stroke-width="3"/><rect x="15" y="18" width="22" height="15" fill="none" stroke="#fff" stroke-width="2"/><polyline points="15,18 26,27 37,18" fill="none" stroke="#fff" stroke-width="2"/></svg>EMAIL UPDATES</div>
  <div class="abs feat" style="left:131px">
    <svg width="52" height="52" viewBox="0 0 52 52"><polygon points="16,1 36,1 51,16 51,36 36,51 16,51 1,36 1,16" fill="#e14b12" stroke="#fff" stroke-width="3"/><rect x="15" y="17" width="22" height="14" rx="3" fill="#fff"/><polygon points="20,31 26,31 19,37" fill="#fff"/></svg>CHIRPER FEED</div>
  <div class="abs feat" style="left:222px">
    <svg width="52" height="52" viewBox="0 0 52 52"><polygon points="16,1 36,1 51,16 51,36 36,51 16,51 1,36 1,16" fill="#b3141b" stroke="#fff" stroke-width="3"/><text x="26" y="24" fill="#fff" font-size="9" font-weight="700" text-anchor="middle" font-family="Arimo,sans-serif">TCLM</text><text x="26" y="35" fill="#fff" font-size="9" font-weight="700" text-anchor="middle" font-family="Arimo,sans-serif">INDEX</text></svg>15 FAB INDEX</div>
  <div class="abs feat" style="left:313px">
    <svg width="52" height="52" viewBox="0 0 52 52"><polygon points="16,1 36,1 51,16 51,36 36,51 16,51 1,36 1,16" fill="#2053a8" stroke="#fff" stroke-width="3"/><rect x="18" y="14" width="16" height="22" fill="#fff"/><g stroke="#2053a8" stroke-width="2"><line x1="21" y1="21" x2="31" y2="21"/><line x1="21" y1="26" x2="31" y2="26"/><line x1="21" y1="31" x2="28" y2="31"/></g></svg>WEEKLY REPORT</div>
  <div class="abs feat" style="left:404px">
    <svg width="52" height="52" viewBox="0 0 52 52"><polygon points="16,1 36,1 51,16 51,36 36,51 16,51 1,36 1,16" fill="#2e8a17" stroke="#fff" stroke-width="3"/><rect x="16" y="15" width="20" height="22" fill="#fff"/><g fill="#2e8a17"><rect x="19" y="27" width="3" height="7"/><rect x="24" y="23" width="3" height="11"/><rect x="29" y="19" width="3" height="15"/></g></svg>MARKET NEWS</div>
</section>

<aside class="abs login">
  <h2>Member Account Login</h2>
  <p class="note">Please login to access our members only content</p>
  <hr>
  <div class="field">User Name: <i></i></div>
  <div class="field">Password: <i></i></div>
  <hr>
  <span class="btn">Submit</span>
  <p class="info">To access our TCLM ST Trades, Current Portfolio, Daily Ticker, Market News or Latest Reports pages, you must sign in. The Calm Ledger Merchant allows you to use the service for FREE, for two weeks. To subscribe to our FREE 2 Week Trail click here.</p>
  <p class="call">Call Now <b>555-014-2277</b></p>
  <p class="mail">or Mail <b>info@calmledgermerchant.com</b></p>
</aside>

<h2 class="abs subscribe-head">Calm Ledger Merchant... SUBSCRIBE NOW!</h2>

<div class="abs plan" style="left:193px;background:var(--royal)"><div class="amt"><sup>$</sup>150</div><div class="term">ONE MONTH</div><span class="go" style="color:var(--royal)">Subscribe</span></div>
<div class="abs plan" style="left:326px;background:var(--orange)"><div class="amt"><sup>$</sup>350</div><div class="term">ONE QUARTER</div><span class="go" style="color:var(--orange)">Subscribe</span></div>
<div class="abs plan" style="left:467px;background:var(--green)"><div class="amt"><sup>$</sup>975</div><div class="term">ONE YEAR</div><span class="go" style="color:var(--green)">Subscribe</span></div>
<div class="abs plan" style="left:598px;background:var(--amber)"><div class="amt"><sup>$</sup>0.00</div><div class="term">TWO WEEK</div><span class="go" style="color:var(--amber)">Subscribe</span></div>

<div class="abs trial">
  <div class="abs trial-photo" role="img" aria-label="Smiling support agent wearing a headset"></div>
  <div class="abs trial-text"><b>FREE 2 WEEK TRIAL</b><span class="gold">LIMITED TIME OFFER!</span><div class="hrs">Please call us during business hours.</div><div class="num">555-014-2277</div></div>
</div>

<section class="abs welcome">
  <h1>Welcome To The Calm Ledger Merchant</h1>
  <p>Dear Investor,</p>
  <p><a href="#">Our Team of Researchers, Stock Traders and Contributors</a> would like to welcome you to "The Calm Ledger Merchant", an opportunity to receive research and opinions on companies and stocks that will outperform the market!!</p>
  <p>If you are an investor or stock trader looking for <a href="#">high quality investment ideas with strong fundamentals to support them</a>, look no further than the "<a class="u" href="#">The Calm Ledger Merchant</a>" as an invaluable resource of investment information. Our approach combines fundamental and technical analysis in order to introduce fresh and successful ideas to our readers.</p>
</section>

<aside class="abs quote">
  <h3>What our Client says,</h3>
  <p><b>I've been a subscriber since April 2014</b> and what a ride it's been!. I have in the past subscribed to a number of investment newsletters and advisory services and blown a lot of money along the way, without any tangible results to show. Thus far I can see real results in my portfolio which sometimes is hard to believe......</p>
  <div class="by">Comment by - Dorian</div>
  <div class="abs arrows">‹ ›</div>
</aside>

<div class="abs cta cta-trial"><div class="big">GET YOUR <b>2</b> WEEK FREE TRIAL</div><div class="small">Subscribe for Two Week FREE trial today</div></div>

<div class="abs cta cta-news">
  <div class="lbl">Subscribe to our newsletter</div>
  <div class="row"><div class="in">First Name <span>*</span></div><div class="in">Email <span>*</span></div><div class="send">SUBMIT</div></div>
</div>

<footer class="abs footer">
  <nav><a href="#">HOME</a> <a href="#">ABOUT</a> <a href="#">CURRENT PORTFOLIO</a> <a href="#">LATEST REPORT</a> <a href="#">WATCHLIST</a> <a href="#">DAILY TICKER</a> <a href="#">MARKET NEWS</a> <a href="#">DISCLAIMER</a></nav>
  <small>©Copyright 2015 The Calm Ledger Merchant. All Rights Reserved.TCLM Publishing, LLC</small>
</footer>
</body>
</html>
```